Motivational Quotes Poster Series

This is a 3 poster design series for Ridgeway Haul Academy. The size of each poster should be 18 inches wide and 24 inches tall. The goal of these posters is to serve as motivational "signs" to be hung in the office area for the employees (not customers). These employees are instructors/teachers, teaching students how to drive semi trucks. While each design is a separate poster and design, we're posting as 1 project because we'd like some continuity between the series. Below we'll break down the details of all 3 posters...

Poster #1
Text that must appear on poster - "If You Want The Best Out Of Each Student" and "Give The Best Of You!" Note: While this text must appear on the poster, you can arrange in the layout as you see fit. For example, first line could be at top of poster and second line on bottom.

Poster #2
Text that must appear on poster - "Invest In People" and "Change Someone's Life" (same notes apply as in 1st poster)

Poster #3
Text that must appear on poster - "Today Is..." and "Just Another Day For You" and "The Most Important Day In Their Life" Note: This can be laid out on the poster however you see fit, but each phrase needs to be separate and it needs to flow.

Target Market(s)

Truck Driver Training Instructors - These are middle-aged, mostly male, masculine type personalities.

Industry/Entity Type

Training

Requirements
Must have
• Must have noted text from description
Must have working files (ie - PSD, EPS, AI, etc) provided
Must have common theme between each poster in series
Must have easy to read font and layout
Must have product dimensions of 18 inches (width) by 24 inches (height). If design uses full dimensions please include quarter inch bleed.
Nice to have
• Nice to have a trucking theme...related to trucking industry, but not over the top. Example - This could mean subtle injection of background tire tracks, but by no means are tire tracks required.

For inspiration, you can visit the site at http://www.ridgewayhaulacademy.com. While you can use the colors of the site/logo, you can still branch out between each poster to try new colors within reason.

Note: While we've attached the logo to this project, it COULD be used but doesn't HAVE to be included in the design. The logo IS NOT a focal point. The phrases in the poster ARE the focal point.

```html
<!DOCTYPE html>
<html lang="en">
<head>
<meta charset="utf-8">
<title>Invest In People – Ridgeway Haul Academy</title>
<link rel="stylesheet" href="https://fonts.googleapis.com/css2?family=Arvo:wght@700&family=Arimo:wght@400;700&display=swap">
<style>
  :root {
    --paper: #ffffff;
    --mist: #d9d9d9;
    --accent-red: #c8171e;
    --ink: #111111;
    --arrow: #8e1b1b;
    --blue: #1a8fd6;
    --green: #5aa832;
    --mauve: #a58aa6;
    --stripe: #b9dcf2;
    --truck: #c9d3dc;
    --logo-ink: #2b2b2b;
  }
  html, body {
    margin: 0;
    padding: 0;
    overflow: hidden;
  }
  body {
    width: 900px;
    height: 1200px;
  }
  .poster {
    position: relative;
    width: 900px;
    height: 1200px;
    overflow: hidden;
    background: linear-gradient(to bottom, var(--mist) 0, #efefef 150px, var(--paper) 330px, var(--paper) 100%);
  }
  .headline {
    position: absolute;
    top: 100px;
    left: 88px;
    margin: 0;
    font-family: "Arvo", serif;
    font-weight: 700;
    line-height: 1;
    white-space: nowrap;
  }
  .headline__lead {
    color: var(--accent-red);
    font-size: 88px;
  }
  .headline__rest {
    color: var(--ink);
    font-size: 62px;
  }
  .flow-arrows {
    position: absolute;
    top: 180px;
    left: 660px;
    width: 160px;
    height: 400px;
  }
  .message {
    position: absolute;
    margin: 0;
    line-height: 1;
    white-space: nowrap;
  }
  .message--change {
    top: 588px;
    left: 322px;
    font-family: "Arvo", serif;
    font-weight: 700;
    font-size: 99px;
    color: var(--blue);
  }
  .message--life {
    top: 718px;
    left: 150px;
    font-family: "Arimo", sans-serif;
    font-weight: 700;
    font-size: 56px;
    color: var(--green);
  }
  .message--life .life-word {
    margin-left: 90px;
    color: var(--mauve);
    font-weight: 400;
    font-size: 90px;
    letter-spacing: 6px;
  }
  .brand {
    position: absolute;
    top: 975px;
    right: 30px;
    display: flex;
    align-items: center;
    gap: 8px;
    font-family: "Arimo", sans-serif;
    font-weight: 700;
    font-size: 18px;
    color: var(--logo-ink);
    white-space: nowrap;
  }
  .brand__mark {
    width: 22px;
    height: 22px;
    background: var(--logo-ink);
  }
  .truck-art {
    position: absolute;
    left: 8px;
    top: 1025px;
    width: 170px;
    height: 90px;
    background: linear-gradient(to bottom, #e6ecf1, var(--truck));
  }
  .road-stripes {
    position: absolute;
    left: 225px;
    top: 1040px;
    width: 675px;
    height: 62px;
    display: flex;
    gap: 14px;
  }
  .road-stripes span {
    flex: 1;
    background: var(--stripe);
  }
</style>
</head>
<body>
  <main class="poster">
    <h1 class="headline">
      <span class="headline__lead">INVEST</span>
      <span class="headline__rest">IN PEOPLE</span>
    </h1>

    <svg class="flow-arrows" viewBox="0 0 160 400" aria-hidden="true">
      <g fill="none" stroke="var(--arrow)" stroke-width="4" stroke-dasharray="16 9">
        <path d="M30 0 C 45 120, 25 260, 45 385"/>
        <path d="M75 0 C 95 130, 72 270, 88 385"/>
        <path d="M115 0 C 130 130, 118 270, 125 385"/>
      </g>
      <g fill="var(--arrow)">
        <polygon points="37,380 55,380 46,398"/>
        <polygon points="79,380 97,380 88,398"/>
        <polygon points="116,380 134,380 125,398"/>
      </g>
    </svg>

    <p class="message message--change">CHANGE</p>
    <p class="message message--life">Someone's<span class="life-word">LIFE</span></p>

    <div class="brand">
      <span class="brand__mark"></span>
      <span class="brand__name">Ridgeway Haul Academy</span>
    </div>

    <div class="truck-art" role="img" aria-label="Illustration of a semi truck with a white trailer"></div>

    <div class="road-stripes" aria-hidden="true">
      <span></span><span></span><span></span><span></span><span></span><span></span>
      <span></span><span></span><span></span><span></span><span></span><span></span>
      <span></span><span></span><span></span><span></span><span></span><span></span>
    </div>
  </main>
</body>
</html>
```